Lantern Hearthworks Business Cards

Looking to create simple business cards that highlight our unique three sided triangle fire pit design with the colors and font of our logo, listed below.

Requirements
Must have
• Looking for something simple that includes a picture of our fire pit with name, website (lanternhearthworks.com), phone number and email. Want to keep the color mostly orange and black.
• Font is gotham(medium) and orange color code is #ee6e22

```html
<!DOCTYPE html>
<html lang="en">
<head>
<meta charset="UTF-8">
<title>Lantern Hearthworks Business Cards</title>
<link href="https://fonts.googleapis.com/css2?family=Montserrat:wght@500&family=Work+Sans:wght@400&display=swap" rel="stylesheet">
<style>
  :root {
    --stage: #1a1a1a;
    --card: #262626;
    --orange: #ee6e22;
    --orange-soft: rgba(238,110,34,.85);
    --white: #f2f2f2;
    --rule: #d8d8d8;
  }
  * { margin: 0; padding: 0; box-sizing: border-box; }
  html, body { width: 1200px; height: 900px; overflow: hidden; background: var(--stage); }
  .sheet { position: relative; width: 1200px; height: 900px; }
  .card {
    position: absolute; left: 250px; width: 700px; height: 400px;
    background: var(--card); border-radius: 3px; overflow: hidden;
    box-shadow: 0 10px 30px rgba(0,0,0,.5);
  }
  .card--front { top: 30px; }
  .card--back { top: 470px; }

  .lockup { position: absolute; display: flex; align-items: center; z-index: 1; }
  .lockup__mark { border-radius: 50%; background: var(--orange); flex: none; }
  .lockup__rule { width: 1.5px; background: var(--rule); margin: 0 22px; flex: none; }
  .lockup__name {
    font-family: "Montserrat", sans-serif; font-weight: 500; color: var(--orange);
    text-transform: uppercase; line-height: 1.05;
  }
  .card--front .lockup { left: 50%; top: 50%; transform: translate(-50%, -50%); }
  .card--front .lockup__mark { width: 62px; height: 62px; }
  .card--front .lockup__rule { height: 110px; }
  .card--front .lockup__name { font-size: 30px; letter-spacing: 7px; }

  .card--back .lockup { left: 60px; top: 44px; }
  .card--back .lockup__mark { width: 40px; height: 40px; }
  .card--back .lockup__rule { height: 80px; margin: 0 16px; }
  .card--back .lockup__name { font-size: 20px; letter-spacing: 5px; }

  .flame-art {
    position: absolute; left: 430px; top: 60px; width: 270px; height: 340px;
    background:
      radial-gradient(ellipse 60% 70% at 55% 70%, var(--orange-soft) 0%, rgba(238,110,34,.45) 45%, rgba(238,110,34,0) 75%);
  }

  .person { position: absolute; left: 90px; top: 200px; z-index: 1; }
  .person__name {
    font-family: "Montserrat", sans-serif; font-weight: 500; font-size: 28px;
    color: var(--orange); text-transform: uppercase; letter-spacing: .5px;
  }
  .person__title {
    font-family: "Work Sans", sans-serif; font-size: 17px; color: var(--white);
    letter-spacing: 1px; margin-top: 2px;
  }
  .person__accent { width: 28px; height: 2px; background: var(--orange); margin-top: 14px; }

  .contacts { position: absolute; left: 76px; top: 298px; list-style: none; z-index: 1; }
  .contacts li {
    display: flex; align-items: center; gap: 10px;
    font-family: "Work Sans", sans-serif; font-size: 18px; color: var(--white);
    letter-spacing: .5px; line-height: 28px;
  }
  .contacts svg { width: 12px; height: 12px; flex: none; }
  .contacts .accent { color: var(--orange); }
</style>
</head>
<body>
<main class="sheet">
  <section class="card card--front" aria-label="Business card front">
    <div class="lockup">
      <span class="lockup__mark"></span>
      <span class="lockup__rule"></span>
      <span class="lockup__name">Lantern<br>Hearthworks</span>
    </div>
  </section>

  <section class="card card--back" aria-label="Business card back">
    <div class="flame-art" role="img" aria-label="Large orange flame graphic rising from the bottom right corner"></div>

    <div class="lockup">
      <span class="lockup__mark"></span>
      <span class="lockup__rule"></span>
      <span class="lockup__name">Lantern<br>Hearthworks</span>
    </div>

    <div class="person">
      <p class="person__name">Owen Halvorsen</p>
      <p class="person__title">CO-Founder</p>
      <div class="person__accent"></div>
    </div>

    <ul class="contacts">
      <li>
        <svg viewBox="0 0 12 12" aria-hidden="true"><path d="M3 1 L5 3.5 L4 5 Q5 7 7 8 L8.5 7 L11 9 L10 11 Q4 11 1 3 Z" fill="var(--orange)"/></svg>
        503-555-0147
      </li>
      <li>
        <svg viewBox="0 0 12 12" aria-hidden="true"><rect x="1" y="2.5" width="10" height="7" fill="none" stroke="var(--orange)" stroke-width="1.3"/><path d="M1 2.5 L6 6.5 L11 2.5" fill="none" stroke="var(--orange)" stroke-width="1.3"/></svg>
        hello@lanternhearthworks.com
      </li>
      <li>
        <svg viewBox="0 0 12 12" aria-hidden="true"><circle cx="6" cy="6" r="5" fill="none" stroke="var(--orange)" stroke-width="1.2"/><path d="M1 6 H11 M6 1 Q3 6 6 11 M6 1 Q9 6 6 11" fill="none" stroke="var(--orange)" stroke-width="1"/></svg>
        <span>www.<span class="accent">lanternhearthworks</span>.com</span>
      </li>
    </ul>
  </section>
</main>
</body>
</html>
```